Black & White graphic page for Unique Brochure

DESCRIPTION: I need to have a pages redone from a brochure. It is a very eclectic and original style of brochure. (kind of a mix of 19th century advertising and some fantasy) The old page graphics were 6x9 inches in dimensions, but now I need the new ones in a 6x10.5 inch dimension. I have uploaded the old files so you can see what was done before. I also need the graphic to be much better and to theme, the prior image is just thrown together. But you can use as a guide to what needs to be on the page, but i would like you to redesign to make it better and to the required 6 in by 10.5 inches.

black and white images and much of it can be in a drawling or woodcut style. I have also uploaded some of the other pictures in the brochure so that you can match what you’re doing to the other stuff. Also, there are 6 of these graphic pages in all, so if i like your design I would like you to do the other 5 images for an additional cost. Overall the images need to be a bit on the bizarre and creepy side for a mood.

Target Market(s)

weird people, men, theatergoers

Industry/Entity Type

Performing Art

Font styles to use
Decorative

Requirements
Must have
• black and white, size of 6 inches wide by 10.5 inches tall, must look old fashion and kind of spooky and eclectic (I uploaded some samples) its kind of a occult, old snake oil salesman advert. should make the reader distrustful of what they are getting like they may be selling their soul! Border that can be reused on the other pages. Use the Illustration of the top hat guy provided.
Nice to have
• use of old fashioned scrolls, wood cut drawling style, needs to include the text "Have you found what you were looking for yet? Apparently not! Well, perhaps you’d be interested in our miraculous “Ezra Quill Show”, a completely custom themed spectacle that we create just for your group. Admittedly, I failed to mention our toll free number—877-TWIRL-31. My apologies—now grab that phone! We hope you’re ready to move forward and try us without delay! "
Should not have
• NO color. no overly modern,

```html
<!DOCTYPE html>
<html lang="en">
<head>
<meta charset="utf-8">
<title>Have You Found What You Were Looking For Yet?</title>
<link href="https://fonts.googleapis.com/css2?family=Rubik+Dirt&family=Open+Sans:wght@600;700&display=swap" rel="stylesheet">
<style>
  :root {
    --backdrop: #000000;
    --paper: #f7f7f5;
    --ink: #111111;
    --art-dark: #1c1c1c;
    --art-mid: #4a4a4a;
  }
  * { margin: 0; padding: 0; box-sizing: border-box; }
  html, body { width: 1200px; height: 1200px; overflow: hidden; background: var(--backdrop); }
  .canvas { position: relative; width: 1200px; height: 1200px; background: var(--backdrop); }
  .page {
    position: absolute; left: 305px; top: 63px; width: 597px; height: 1043px;
    background: radial-gradient(ellipse at 40% 30%, #ffffff 0%, var(--paper) 70%, #ececea 100%);
    color: var(--ink);
  }
  .page-border {
    position: absolute; left: 18px; top: 20px; width: 560px; height: 1005px;
    border: 2px solid var(--ink);
  }
  .line { position: absolute; left: 0; width: 100%; text-align: center; white-space: nowrap; }
  .headline { top: 52px; font-family: "Rubik Dirt", "Impact", sans-serif; font-size: 54px; line-height: 1; letter-spacing: 0.5px; }
  .subhead { top: 112px; font-family: "Rubik Dirt", "Impact", sans-serif; font-size: 22px; line-height: 1; }
  .art-frame {
    position: absolute; left: 50px; top: 173px; width: 508px; height: 355px;
    border: 3px double var(--ink); outline: 2px solid var(--ink); outline-offset: 6px;
  }
  .art {
    position: absolute; left: 170px; top: 206px; width: 266px; height: 294px;
    border-radius: 40px 40px 0 0 / 20px 20px 0 0;
    background: radial-gradient(ellipse at 50% 45%, var(--art-mid) 0%, var(--art-dark) 65%, #000 100%);
  }
  .callout { top: 558px; font-family: "Rubik Dirt", "Impact", sans-serif; font-size: 34px; line-height: 1; }
  .body-copy {
    position: absolute; left: 40px; top: 608px; width: 520px; text-align: center;
    font-family: "Open Sans", Arial, sans-serif; font-weight: 700; font-size: 17.5px; line-height: 26.4px;
    text-transform: uppercase;
  }
  .divider { position: absolute; left: 125px; top: 739px; }
  .note { top: 771px; font-family: "Open Sans", Arial, sans-serif; font-weight: 700; font-size: 16px; line-height: 1; }
  .phone { top: 806px; font-family: "Rubik Dirt", "Impact", sans-serif; font-size: 60px; line-height: 1; letter-spacing: 1px; }
  .apology { top: 891px; font-family: "Open Sans", Arial, sans-serif; font-weight: 700; font-size: 17px; line-height: 1; }
  .closing {
    position: absolute; left: 30px; top: 930px; width: 540px; text-align: center;
    font-family: "Open Sans", Arial, sans-serif; font-weight: 700; font-size: 17.5px; line-height: 26px;
  }
</style>
</head>
<body>
<div class="canvas">
  <div class="page">
    <div class="page-border"></div>

    <div class="line headline">HAVE YOU FOUND</div>
    <div class="line subhead">WHAT YOU WERE LOOKING FOR YET?</div>

    <div class="art-frame"></div>
    <div class="art" role="img" aria-label="Woodcut illustration of a grinning top-hatted showman pouring potions into a swirling cauldron before stage curtains, surrounded by glass flasks"></div>

    <div class="line callout">APPARENTLY NOT!</div>
    <p class="body-copy">Well, perhaps you’d be interested in our miraculous “Ezra Quill Show”, a completely custom themed spectacle that we create just for your group.</p>

    <svg class="divider" width="346" height="22" viewBox="0 0 346 22" aria-hidden="true">
      <line x1="2" y1="11" x2="128" y2="11" stroke="#111" stroke-width="1.5"/>
      <line x1="218" y1="11" x2="344" y2="11" stroke="#111" stroke-width="1.5"/>
      <circle cx="2" cy="11" r="2.5" fill="#111"/>
      <circle cx="344" cy="11" r="2.5" fill="#111"/>
      <polygon points="173,0 178,11 173,22 168,11" fill="#111"/>
      <circle cx="152" cy="11" r="3" fill="none" stroke="#111" stroke-width="1.5"/>
      <circle cx="194" cy="11" r="3" fill="none" stroke="#111" stroke-width="1.5"/>
    </svg>

    <div class="line note">ADMITTEDLY, I FAILED TO MENTION OUR TOLL FREE NUMBER</div>
    <div class="line phone">877-TWIRL-31</div>
    <div class="line apology">MY APOLOGIES!</div>
    <p class="closing">NOW GRAB THAT PHONE! WE HOPE YOU’RE READY TO MOVE FORWARD AND TRY US WITHOUT DELAY!</p>
  </div>
</div>
</body>
</html>
```